New web/graphic designs required to improve existing ecommerce site.

Initial outline of project:
This project is for new designs to fit into areas of existing webpages - specifically:-
Objective 1 - Produce 8 home page design proposals (design for central area of page only, not whole page)
Objective 2 - Produce 5 designs for page header banners (950px x 84px images)
Objective 3 - Produce 10 designs for help guide covers (316px x 410px images)
Also, on a more general note:
Objective 4 - Review and suggest improvements for other areas website. (This may lead to further design work)
-
Introduction to the Periodical Bazaar website:
The Periodical Bazaar website is a marketplace where back-issue hobby magazines can be bought and sold, and in some cases downloaded & viewed in digital form. The ‘sellers’ of the magazines will be both traders and private individuals. Trade sellers will also be able to sell magazine subscriptions and have ‘Promotion Pages’ about themselves and/or their magazine titles on the site. Other forms of advertising will also be available on the site for any commercial advertisers who want it, particularly for companies supplying the various hobbies covered.
Users of the website can locate magazines of interest to them by browsing through the hobby / category sections of the site, or by doing keyword searches for issues containing articles on specific topics.
The site is split-up into sections dealing with magazines about specific hobby subjects – ie., cars, motorbikes, railway, aviation, boating etc. Although part of the larger site, each of these sections is largely self-contained, with many users only ever browsing in the section related to their hobby. As such, each section effectively has it’s own home page, which will duplicate much of the information shown on the main home page. These multiple ‘section home pages’ will be promoted in their own right via URLs specific to that hobby. Currently there are 8 sections, but this number is expected to increase as the site grows.
This website is still being developed, but is close to launch; as such the website is fully functional but a lot of content is missing - please bear this in mind when viewing the site, and feel free to ask for clarification if anything is unclear.
The new website is currently at: http://www2.periodicalbazaar.co.uk
This website will replace several existing sites:-
http://www.periodicalbazaar.co.uk
http://www.twowheel-quarterlies.co.uk
http://www.skyward-quarterlies.co.uk
http://www.drivezines.co.uk
http://www.trackside-quarterlies.co.uk
http://www.scalecraft-quarterlies.co.uk
-
Design notes:
The overall design is fairly conventional and very much ‘functionality’ driven, the website being at it’s heart an ecommerce system with some fairly complex features. Nevertheless I want the site to appear simple and modern in appearance, being somewhere between an ‘all style’ Web 2.0-type site (eg. tastely.io), and an ‘all function’ conventional trading site (eg. Brindle, Vendo etc). A good example of a style of site which I would like to emulate is PostParrot – a complex and large site made to look friendly and approachable by the use of simple, clear design, bold colour and a sense of humour.
To explain further what is required I have prepared various image documents which include more detailed notes on the various objectives for this project. There is a lot of information in these documents - please read them carefully:-
Objective 1:
- Produce 1 'Main Home Page' design proposal
- Produce 8 'Section Home Page' design proposals - one each for these sections: Railway, Boating, Aviation, Cycling, Automotive, Motorcycling, Men's Lifestyle, Modelling
More information on Objective 1 is given in these image documents:
http://www.filecove.net/Home_Page_Designs-Purpose.gif
http://www.filecove.net/Home_Page_Designs-Areas.gif
http://www.filecove.net/Section_Home_Pages-1.gif
http://www.filecove.net/Section_Home_Pages-2.gif
-
Objective 2:
- Produce 5 designs for page header banners (950px x 84px images)
More information on Objective 2 is given in this image document:
http://www.filecove.net/Page_Header_Banners.gif
-
Objective 3:
- Produce 10 designs for help guide covers (316px x 410px images)
http://www.filecove.net/Help_Guide_Covers.gif
-
Objective 4:
- Review and suggest improvements for other areas website
I would like the designer to spend some time looking at the whole of the current website, and suggest any areas that can be improved. I am not looking for a wholesale re-design - the overall layout of the site and major design elements such as the navigation system - are essentially fixed - however, many graphical elements can be changed, as can any text content (including text content within the navigation system).
Improvements which are suggested may lead to additional design work either as part of this project, or as subsequent projects in their own right.
-
Designers are very welcome to contact me to discuss any aspect of this project, or if more information is required about the website or the designs required.
I'm happy to guarantee this project in due course, if there is positive reaction to the project from potential designers interested in submitting designs. This is the second project I have run on SketchGuild - the first one was successful and resulted in the Flash animation that is currently on the homepage of the website.
UPDATE 11/10/11:
I've created some new documents to illustrate the sort of designs I am looking for for the Main Home Page and Section Home Pages:
Very rough examples of the sort of style I am looking for:
http://www.filecove.net/Rough_Main_Home_Page_1.jpg
http://www.filecove.net/Rough_Main_Home_Page_2.jpg
http://www.filecove.net/Rough_Main_Home_Page_3.jpg
http://www.filecove.net/Rough_Main_Home_Page_4.jpg
http://www.filecove.net/Rough_Main_Home_Page_5.jpg
http://www.filecove.net/Rough_Section_Home_Page.jpg
http://www.filecove.net/Rough_Section_Home_Page_2.jpg
Detailed document showing exact content required for the Main Home Page and each Section Home Page:
http://www.filecove.net/Home_Page_Content.gif
Mainly male, age 20 - 60. Not necessarily 'web savvy' or design-conscious
Advertising

```html
<!DOCTYPE html>
<html lang="en">
<head>
<meta charset="utf-8">
<title>Periodical Bazaar – Home</title>
<link href="https://fonts.googleapis.com/css2?family=Arimo:ital,wght@0,400;0,700;1,400;1,700&display=swap" rel="stylesheet">
<style>
:root{
  --ink:#222;
  --text:#666;
  --orange-top:#fdca3e;
  --orange-bottom:#ef8500;
  --green:#8fb514;
  --green-light:#a6cb2a;
  --heading-green:#7a9a08;
  --dark:#1e1e1e;
  --footer:#2a2a2a;
  --footer-base:#161616;
  --line:#dcdcdc;
}
*{box-sizing:border-box;margin:0;padding:0}
html,body{width:1015px;height:1200px;overflow:hidden}
body{position:relative;background:#fff;font-family:"Arimo",Arial,sans-serif;color:var(--ink)}
.abs{position:absolute}
.topline{left:0;top:0;width:1015px;height:4px;background:#3a3a3a}
.header{left:0;top:4px;width:1015px;height:86px;background:linear-gradient(#fafafa,#ececec)}
.brand{left:50px;top:28px;font-size:22px;font-weight:700;color:#c4161c;letter-spacing:-.5px}
.search-bar{left:773px;top:13px;width:196px;height:26px;background:var(--dark);border-radius:3px;color:#aaa;font-size:11px;font-style:italic;padding:7px 10px}
.search-go{right:4px;top:3px;width:20px;height:20px;border-radius:50%;background:#f7941d}
.account{top:56px;font-size:12px;color:#222}
.checkout{left:895px;top:51px;width:74px;height:23px;background:linear-gradient(#ffd84d,#f7b500);border:1px solid #e09b00;font-size:12px;text-align:center;line-height:21px}
.band{left:0;top:90px;width:1015px;height:223px;background:linear-gradient(var(--orange-top),var(--orange-bottom))}
.nav-rail{left:71px;top:100px;width:3px;height:200px;background:#fff}
.nav-item{left:97px;font-size:14px;font-weight:700;color:#fff;letter-spacing:.3px}
.nav-sep{left:76px;width:140px;height:1px;background:rgba(255,255,255,.45)}
.nav-active{left:76px;top:107px;width:148px;height:20px;background:#f6a81d;border-radius:0 10px 10px 0}
.hero{left:266px;top:105px;width:689px;height:208px;background:linear-gradient(#3fa6e6,#8fd0f5 55%,#5fb83a 75%,#3c8d22)}
.hero-title{left:280px;top:108px;font-size:38px;line-height:42px;color:#111}
.panel{left:266px;top:313px;width:689px;height:649px;background:#fff;box-shadow:0 1px 4px rgba(0,0,0,.2)}
.pill{left:54px;width:174px;height:36px;background:linear-gradient(#3a3a3a,#111);border-radius:6px;color:#fff;font-size:14px;padding:10px 0 0 14px}
.sec{left:70px;font-size:12px;color:#444}
.sec-icon{display:inline-block;width:17px;height:15px;background:#222;border-radius:2px;position:relative;vertical-align:middle;margin-right:10px}
.sec-icon:after{content:"";position:absolute;left:6px;top:4px;border-left:6px solid #fff;border-top:4px solid transparent;border-bottom:4px solid transparent}
.promo{left:47px;top:713px;width:198px;height:87px;background:linear-gradient(#fbb03b,#f58a1f);border:1px solid #e67e00}
.promo-title{left:13px;top:8px;color:#fff;font-size:15px;font-weight:700}
.promo-sub{left:96px;top:30px;color:#fff;font-size:11px;font-style:italic}
.promo-cart{left:12px;top:36px;width:36px;height:38px;background:#6aa624;border-radius:4px}
.promo-btn{left:100px;top:51px;width:83px;height:23px;background:#fff;border:1px solid #ccc;font-size:11px;text-align:center;line-height:21px;color:#333}
.ad{left:47px;top:809px;width:203px;height:153px;background:linear-gradient(135deg,#f2f2ee,#dcdcd6)}
.search-box{left:283px;top:336px;width:196px;height:172px;background:linear-gradient(#fff,#e9e9e9);border:1px solid #d2d2d2;border-radius:6px;box-shadow:0 1px 3px rgba(0,0,0,.15)}
.search-box h3{position:absolute;left:12px;top:12px;font-size:14px;font-weight:400;color:#777}
.field{left:17px;width:156px;height:22px;background:#fff;border:1px solid #ccc;font-size:10px;font-style:italic;color:#999;padding:5px 9px}
.search-btn{left:59px;top:119px;width:78px;height:27px;background:linear-gradient(#7fd6f5,#2aa8de);color:#fff;font-size:12px;font-weight:700;text-align:center;line-height:27px;border:1px solid #1c93c7}
.welcome{left:498px;top:337px;width:441px;height:171px;border:1px solid var(--line);background:#fff;padding:5px}
.welcome-inner{width:429px;height:159px;background:linear-gradient(135deg,var(--green-light),var(--green));position:relative}
.welcome h2{position:absolute;left:12px;top:12px;font-size:19px;font-style:italic;font-weight:700;color:#fff}
.welcome .tag{position:absolute;right:28px;top:55px;font-size:14px;font-style:italic;font-weight:700;color:#3d5200}
.action{position:absolute;top:94px;width:87px;height:29px;border-radius:8px;background:linear-gradient(#fff,#d8d8d8);box-shadow:0 2px 0 #888;font-size:13px;color:#444;text-align:center;line-height:29px}
.action-note{position:absolute;top:131px;width:87px;font-size:10px;color:#3d5200;text-align:center}
.article{left:283px;width:660px}
.article h4{font-size:13px;font-weight:400;color:var(--heading-green);padding-left:13px;position:relative}
.article h4:before{content:"";position:absolute;left:0;top:2px;border-left:6px solid #333;border-top:5px solid transparent;border-bottom:5px solid transparent}
.article p{margin-top:11px;font-size:9.6px;line-height:14px;color:var(--text)}
.rule{left:279px;width:663px;height:1px;background:var(--line)}
.catbar{left:0;top:976px;width:1015px;height:46px;background:linear-gradient(#4a4a4a,#1d1d1d)}
.cat{top:991px;width:100px;text-align:center;font-size:12px;color:#fff}
.cat-sep{top:978px;width:1px;height:42px;background:#555}
.footer{left:0;top:1022px;width:1015px;height:128px;background:var(--footer)}
.foot-h{top:1043px;font-size:11px;font-weight:700;color:#fff}
.foot-l{font-size:10.5px;color:#bbb;line-height:18.5px}
.foot-div{left:553px;top:1040px;width:1px;height:96px;background:#666}
.base{left:0;top:1150px;width:1015px;height:50px;background:var(--footer-base)}
.copy{left:51px;top:1169px;font-size:11px;color:#fff}
.connect{left:707px;top:1169px;font-size:11px;color:#fff}
.social{top:1162px;width:24px;height:24px;border-radius:3px}
</style>
</head>
<body>
<div class="abs topline"></div>
<header class="abs header"></header>
<div class="abs brand">periodicalbazaar.co.uk</div>
<div class="abs search-bar">Search...<span class="abs search-go"></span></div>
<div class="abs account" style="left:660px">Hello Guest</div>
<div class="abs account" style="left:733px">|&nbsp;&nbsp;&nbsp;&nbsp;Log in</div>
<div class="abs account" style="left:794px">|&nbsp;&nbsp;&nbsp;&nbsp;My Basket (0)</div>
<div class="abs checkout">Check Out</div>

<div class="abs band"></div>
<div class="abs nav-active"></div>
<div class="abs nav-rail"></div>
<div class="abs nav-item" style="top:110px">HOME</div>
<div class="abs nav-sep" style="top:133px"></div>
<div class="abs nav-item" style="top:143px">BUY</div>
<div class="abs nav-sep" style="top:166px"></div>
<div class="abs nav-item" style="top:176px">SELL</div>
<div class="abs nav-sep" style="top:199px"></div>
<div class="abs nav-item" style="top:209px">MY MAGS</div>
<div class="abs nav-sep" style="top:232px"></div>
<div class="abs nav-item" style="top:243px">HELP</div>
<div class="abs nav-sep" style="top:266px"></div>
<div class="abs nav-item" style="top:276px">ALL MAGAZINES</div>

<div class="abs hero" role="img" aria-label="Cartoon hobby landscape with a mechanic character holding a car magazine, mountains, quad bike and golf green"></div>
<div class="abs hero-title">Have a<br>&nbsp;&nbsp;&nbsp;&nbsp;&nbsp;&nbsp;&nbsp;hobby?</div>

<div class="abs panel"></div>

<div class="abs pill" style="top:322px">Browse main sections:</div>
<div class="abs sec" style="top:374px"><span class="sec-icon"></span>Aviation</div>
<div class="abs sec" style="top:411px"><span class="sec-icon"></span>Automotive</div>
<div class="abs sec" style="top:448px"><span class="sec-icon"></span>Railway</div>
<div class="abs sec" style="top:485px"><span class="sec-icon"></span>Cycling</div>
<div class="abs sec" style="top:522px"><span class="sec-icon"></span>Boating</div>
<div class="abs sec" style="top:559px"><span class="sec-icon"></span>Modelling</div>
<div class="abs sec" style="top:596px"><span class="sec-icon"></span>Men's lifestyle</div>
<div class="abs sec" style="top:633px"><span class="sec-icon"></span>Motorcycling</div>
<div class="abs pill" style="top:665px">Quick Link to Others
  <svg class="abs" style="left:150px;top:15px" width="12" height="7"><path d="M0 0h12L6 7z" fill="#fff"/></svg>
</div>

<div class="abs promo">
  <div class="abs promo-title">Sell your magazines</div>
  <div class="abs promo-sub">on this website</div>
  <div class="abs promo-cart" role="img" aria-label="Shopping cart illustration"></div>
  <div class="abs promo-btn">Learn more &raquo;</div>
</div>
<div class="abs ad" role="img" aria-label="Online degree advertisement with a relaxing student"></div>

<div class="abs search-box">
  <h3>Article Search</h3>
  <div class="abs field" style="top:40px">Key words</div>
  <div class="abs field" style="top:77px">All Sections</div>
  <div class="abs search-btn">Search</div>
</div>

<div class="abs welcome">
  <div class="welcome-inner">
    <h2>Welcome To Periodical Bazaar</h2>
    <div class="tag">Using this website you can...</div>
    <div class="action" style="left:10px">Search</div><div class="action-note" style="left:10px">For Articles</div>
    <div class="action" style="left:112px">Buy</div><div class="action-note" style="left:112px">Back Issues</div>
    <div class="action" style="left:215px">Sell</div><div class="action-note" style="left:215px">Your magazines</div>
    <div class="action" style="left:317px">Read</div><div class="action-note" style="left:317px">Issues Online</div>
  </div>
</div>

<section class="abs article" style="top:533px">
  <h4>Back Issue Hobby Magazines</h4>
  <p>Periodical Bazaar sells back-issue magazines covering hobby subjects including Automotive, Aviation, Railway, Modelling, Motorbiking, Boating, Cycling and Men's Lifestyle. Each section on our website contains dozens of magazine titles from different publishers. Use the left menu to start browsing our site…or alternatively use the…</p>
</section>
<div class="abs rule" style="top:612px"></div>
<section class="abs article" style="top:626px">
  <h4>Magazine Article Search Facility</h4>
  <p>Use the Search facility (in the horizontal black bar above) to find magazine issues containing articles on specific topics. To improve relevance you can filter your search by Section (if searching from this page), or by Category or Title (if searching from within a Section)</p>
</section>
<div class="abs rule" style="top:692px"></div>
<section class="abs article" style="top:706px">
  <h4>About Us – Buy Old Magazines Online</h4>
  <p>Periodical Bazaar is UK-based, and is an independent company offering magazines from many different publishers. At the heart of our service is a unique database of magazine issues &amp; articles covering thousands of titles stretching back to the 1950s. As well as listing our own large stocks, this website allows other private &amp; trade sellers to offer their old magazines for sale. Magazine back issues – and in some cases current issues &amp; subscriptions too – may be ordered from this site for mail-order delivery around the world</p>
</section>
<div class="abs rule" style="top:801px"></div>
<section class="abs article" style="top:814px">
  <h4>Sell Your Magazines</h4>
  <p>Use this website to sell your old magazine collection for cash - click the button in the yellow box above for more information</p>
</section>
<div class="abs rule" style="top:864px"></div>
<section class="abs article" style="top:880px">
  <h4>Magazine Subscriptions &amp; Digital Issues</h4>
  <p>Subscriptions for many magazine titles may be purchased through this website, for yourself or as an ideal gift. In some cases individual magazine issues may also be downloaded in digital form.</p>
</section>

<nav class="abs catbar"></nav>
<div class="abs cat" style="left:60px">Aviation</div>
<div class="abs cat-sep" style="left:170px"></div>
<div class="abs cat" style="left:171px">Automotive</div>
<div class="abs cat-sep" style="left:280px"></div>
<div class="abs cat" style="left:282px">Railway</div>
<div class="abs cat-sep" style="left:381px"></div>
<div class="abs cat" style="left:383px">Cycling</div>
<div class="abs cat-sep" style="left:480px"></div>
<div class="abs cat" style="left:483px">Boating</div>
<div class="abs cat-sep" style="left:585px"></div>
<div class="abs cat" style="left:589px">Modelling</div>
<div class="abs cat-sep" style="left:692px"></div>
<div class="abs cat" style="left:712px">Men's lifestyle</div>
<div class="abs cat-sep" style="left:828px"></div>
<div class="abs cat" style="left:843px">Motorcycling</div>

<footer class="abs footer"></footer>
<div class="abs foot-h" style="left:54px">ABOUT US</div>
<div class="abs foot-l" style="left:54px;top:1065px">Who We Are<br>Our Service<br>Careers<br>Contact us</div>
<div class="abs foot-h" style="left:148px">BUYING MAGAZINES</div>
<div class="abs foot-l" style="left:148px;top:1065px">Buying Back Issues<br>Buying Subscriptions<br>Buying FAQ's</div>
<div class="abs foot-h" style="left:288px">SELLING MAGAZINES</div>
<div class="abs foot-l" style="left:288px;top:1065px">New Seller Overview<br>Seller Terms &amp; Conditions<br>Publisher Services<br>Register / Log-In</div>
<div class="abs foot-h" style="left:445px">ADVERTISING</div>
<div class="abs foot-l" style="left:445px;top:1065px">Advertising Overview<br>Rate Card<br>Make Booking</div>
<div class="abs foot-div"></div>
<div class="abs foot-h" style="left:572px">CONTACT US</div>
<div class="abs foot-l" style="left:572px;top:1065px">Periodical Bazaar,<br>12 Mill Lane, Ashby Vale,<br>Derbyshire, DE99 4XY, UK.</div>
<div class="abs foot-l" style="left:779px;top:1065px">Call Us : 01632 960418<br><br style="line-height:8px">Email : Orders@periodicalbazaar.co.uk</div>

<div class="abs base"></div>
<div class="abs copy">Copyright © 2004-2011 Periodical Bazaar. All Rights Reserved</div>
<div class="abs connect">Connect with us :</div>
<div class="abs social" style="left:791px;background:#3b5a9a" aria-label="Facefolio"></div>
<div class="abs social" style="left:828px;background:#3fb3e0" aria-label="Chirpline"></div>
<div class="abs social" style="left:866px;background:#f26a21" aria-label="Postpad"></div>
<div class="abs social" style="left:904px;background:#1b78b4" aria-label="Linkwork"></div>
<div class="abs social" style="left:942px;background:#6a9a2c" aria-label="Searchly"></div>
</body>
</html>
```